Velmorytrips.com web design project + logo design

Hi,

We are a Russian online tour operator - roamquiltex.com

We are looking to tranmsfer our domain to velmorytrips.com. The website and logo need to be velmoryesque - we are not looking to change our functionality, but we need to make the website much more attracitve to clients, much more wild looking but at the same time remaining a professional travel company.

The main concept of the website should be innovative travel (as velmory was an innovator). Alternatively, you could go down the artist route and go down the draw / design your own tour road.

On our website the customer is able to combine travel services (hotels, flights, Visa services, and soon chauffeur, car rental etc...) put it into their basket (the basket definitely has to look better than it is at the moment) and pay for it in one go by card.

We are also stressin our customer support with web chat, call centre etc... (call centre number at the top of the page)

We aim to provide an easy user experience, but we need to make it have some more style, so I will be waiting for what you guys can come up with.
Let me know if you have any questions - skype is: mrkostelin

Industry/Entity Type

It Company

Logo Text

Requirements
Must have
• It is quite a simple task - to take the existing website roamquiltex.com and velmorysize it to create velmorytrips.com, the functionality of the website will remain the same and there are not many pages in the website. Homepage, Checkout step1, Checkout step 2 (you can view both of these if you select a service) and the generic pages for T&C''s, Privacy policy etc...

IMPORTANT UPDATE

We are also looking at how the search results will look in the designs, (please do a search on our website for hotel / flight)

```html
<!DOCTYPE html>
<html lang="en">
<head>
<meta charset="utf-8">
<title>Velmorytrips.com</title>
<link href="https://fonts.googleapis.com/css2?family=Open+Sans:wght@400;600;700&family=PT+Sans:wght@400;700&display=swap" rel="stylesheet">
<style>
:root{
  --page:#eeeced;
  --header:#e1dfdf;
  --nav-grey:#a29fa0;
  --blue-top:#2f6cf0;
  --blue-bottom:#0b2c8e;
  --panel:#465a9a;
  --field:#f2eff0;
  --field-line:#c9c6c7;
  --form-bg:#e4e3e3;
  --green:#478a26;
  --green-light:#6cbb45;
  --tickets:#445694;
  --gold:#b38e13;
  --footer:#333333;
  --footer-bottom:#2b2b2b;
  --footer-head:#e8e8e8;
  --footer-link:#a8a8a8;
  --text-dark:#333333;
  --phone-blue:#2b2fa6;
  --brand-ink:#111111;
}
*{box-sizing:border-box;margin:0;padding:0}
html,body{width:1200px;height:1023px;overflow:hidden}
body{position:relative;background:var(--page);font-family:"Open Sans",Arial,sans-serif;color:var(--text-dark)}
.abs{position:absolute}

.site-header{left:0;top:0;width:1200px;height:94px;background:var(--header)}
.brand{left:56px;top:-66px;width:250px;height:238px;border-radius:50%;background:#fff;z-index:3;
  display:flex;align-items:flex-end;justify-content:center;padding-bottom:64px}
.brand-name{font-family:"Open Sans",Arial,sans-serif;font-weight:700;font-size:26px;color:var(--brand-ink);letter-spacing:-0.5px;line-height:1}

.nav-btn{top:21px;height:59px;color:#fff;font-size:15px;text-align:center;line-height:72px;background:var(--nav-grey)}
.nav-form{left:360px;width:136px;background:linear-gradient(var(--blue-top),var(--blue-bottom));color:#d6e0ff}
.nav-tour{left:506px;width:137px}
.nav-lang{left:652px;width:138px}
.nav-form svg{position:absolute;left:53px;top:5px}

.contact{right:73px;top:22px;text-align:right}
.contact .hours{font-size:11px;color:#222;font-family:"PT Sans",Arial,sans-serif}
.contact .phone-city{font-size:13px;color:var(--phone-blue);margin-top:8px}
.contact .phone-free{font-size:18px;color:#555;margin-top:-2px}

.hero{left:0;top:94px;width:1200px;height:531px;
  background:linear-gradient(180deg,#8a70c9 0%,#a26bbd 40%,#8c5a8e 65%,#4a3044 82%,#3a2a33 100%)}

.search-panel{left:390px;top:308px;width:668px;height:294px;background:var(--panel);border-radius:8px}
.tab{left:401px;width:125px;height:61px;font-family:"PT Sans",Arial,sans-serif;font-weight:700;font-size:15px;display:flex;align-items:center;padding-left:20px;gap:14px}
.tab-flights{top:334px;background:#e6e5e5;color:#555}
.tab-hotels{top:398px;background:var(--green-light);color:#fff}
.tab-info{top:462px;background:linear-gradient(var(--green-light),#4f9b2c);color:#fff;padding-left:56px}
.form-card{left:512px;top:334px;width:529px;height:256px;background:var(--form-bg);border-radius:8px}

.label{font-size:11.5px;color:#333}
.field{height:30px;width:119px;background:var(--field);border:1px solid var(--field-line);border-radius:4px;font-size:13px;padding-left:16px;line-height:28px}
.select{top:507px;height:33px;width:83px;background:#f3f2f2;border:1px solid var(--field-line);border-radius:3px;font-size:12px;color:#555}
.select span{position:absolute;left:22px;top:8px}
.select i{position:absolute;right:0;top:0;width:34px;height:31px;border-left:1px solid var(--field-line)}
.select svg{position:absolute;left:11px;top:12px}
.radio{width:13px;height:13px;border-radius:50%;background:#f5f5f5;border:1px solid #bbb}
.radio-label{font-size:11.5px}
.search-btn{left:922px;top:510px;width:106px;height:70px;border-radius:4px;background:linear-gradient(var(--blue-top),var(--blue-bottom));color:#fff;font-size:13px;text-align:center;line-height:70px}

.tile{top:632px;height:148px;color:#fff;font-size:38px;display:flex;align-items:center;justify-content:center;letter-spacing:0.5px}
.tile-hotels{left:74px;width:339px;background:var(--green)}
.tile-tickets{left:427px;width:350px;background:var(--tickets)}
.tile-info{left:791px;width:338px;background:var(--gold)}

.site-footer{left:0;top:815px;width:1200px;height:169px;background:var(--footer)}
.footer-col h3{font-weight:400;font-size:15px;color:var(--footer-head);margin-bottom:20px}
.footer-col li{list-style:none;font-size:13px;color:var(--footer-link);line-height:21px}
.social{top:903px;width:64px;height:64px;border-radius:50%;display:flex;align-items:center;justify-content:center;font-size:11px;color:#fff;font-weight:600}
.social-kin{left:874px;background:#4a5b8c}
.social-chirpa{left:967px;background:#8e8e8e}
.social-workly{left:1059px;background:#5a5a5a}
.footer-bar{left:0;top:984px;width:1200px;height:39px;background:var(--footer-bottom);color:#4a4a4a;font-size:14px;text-align:center;line-height:39px}
</style>
</head>
<body>

<header class="abs site-header"></header>
<div class="abs brand">
  <div class="brand-name">velmorytravel</div>
</div>

<nav>
  <div class="abs nav-btn nav-form">
    <svg width="30" height="18" viewBox="0 0 30 18"><ellipse cx="15" cy="7" rx="13" ry="6.5" fill="#e8ecf8"/><path d="M8 11 L6 17 L13 12 Z" fill="#e8ecf8"/></svg>
    FORM
  </div>
  <div class="abs nav-btn nav-tour">MY TOUR</div>
  <div class="abs nav-btn nav-lang">LANGUAGE</div>
</nav>

<div class="abs contact">
  <div class="hours">(Mon-Fri) Hours: 9:00 am - 18:00</div>
  <div class="phone-city">+7 (495) 555-01-27</div>
  <div class="phone-free">8-800-555-0142</div>
</div>

<section class="abs hero" role="img" aria-label="Night view of Paris with the illuminated Eiffel Tower, river and lit high-rise towers under a purple sky"></section>

<section class="abs search-panel"></section>
<div class="abs tab tab-flights">
  <svg width="20" height="18" viewBox="0 0 20 18"><path d="M2 16 L18 2 M8 4 L14 8 L11 11 M4 9 L8 12 L6 14" stroke="#555" stroke-width="2.5" fill="none"/></svg>
  Flights
</div>
<div class="abs tab tab-hotels">
  <svg width="24" height="14" viewBox="0 0 24 14"><rect x="1" y="1" width="2.5" height="12" fill="#fff"/><rect x="1" y="7" width="22" height="3" fill="#fff"/><rect x="21" y="6" width="2.5" height="7" fill="#fff"/><rect x="5" y="3" width="5" height="3" fill="#fff"/><rect x="11" y="3" width="10" height="3" fill="#fff"/></svg>
  Hotels
</div>
<div class="abs tab tab-info">Info</div>
<div class="abs form-card"></div>

<div class="abs label" style="left:590px;top:365px">Whence</div>
<div class="abs field" style="left:589px;top:381px"></div>
<div class="abs label" style="left:783px;top:365px">Where</div>
<div class="abs field" style="left:782px;top:381px"></div>

<div class="abs label" style="left:592px;top:422px">There</div>
<div class="abs field" style="left:589px;top:439px">15-06-2013</div>
<div class="abs label" style="left:786px;top:422px">Back</div>
<div class="abs field" style="left:782px;top:439px"></div>

<div class="abs radio" style="left:917px;top:434px"></div>
<div class="abs radio-label" style="left:938px;top:432px">Back</div>
<div class="abs radio" style="left:917px;top:454px"></div>
<div class="abs radio-label" style="left:937px;top:455px">One way</div>

<div class="abs label" style="left:595px;top:487px">Adults</div>
<div class="abs select" style="left:590px"><span>1</span><i><svg width="12" height="8" viewBox="0 0 12 8"><path d="M2 2 L6 6 L10 2" stroke="#555" stroke-width="2" fill="none"/></svg></i></div>
<div class="abs label" style="left:683px;top:487px">Children</div>
<div class="abs select" style="left:682px"><span>1</span><i><svg width="12" height="8" viewBox="0 0 12 8"><path d="M2 2 L6 6 L10 2" stroke="#555" stroke-width="2" fill="none"/></svg></i></div>
<div class="abs label" style="left:787px;top:487px">Class</div>
<div class="abs field" style="left:782px;top:510px;font-size:12px;color:#888;padding-left:8px">Economy</div>

<div class="abs search-btn">SEARCH</div>

<section>
  <div class="abs tile tile-hotels">HOTELS</div>
  <div class="abs tile tile-tickets">TICKETS</div>
  <div class="abs tile tile-info">INFO</div>
</section>

<footer class="abs site-footer"></footer>
<div class="abs footer-col" style="left:80px;top:848px">
  <h3>View Site</h3>
  <ul><li>Home</li><li>About Us</li><li>Forum</li><li>Contacts</li></ul>
</div>
<div class="abs footer-col" style="left:297px;top:851px">
  <h3>Help</h3>
  <ul><li>Help</li><li>Terms of use</li><li>Privacy Policy</li><li>Cookies</li></ul>
</div>
<div class="abs footer-col" style="left:512px;top:854px">
  <h3>Find us</h3>
  <ul><li>Roamquiltex Limited</li><li>14 Harlow Street</li><li>London, N4 2QX</li></ul>
</div>
<div class="abs footer-col" style="left:880px;top:859px"><h3>We are in</h3></div>
<div class="abs social social-kin">Kinbook</div>
<div class="abs social social-chirpa">Chirpa</div>
<div class="abs social social-workly">Workly</div>
<div class="abs footer-bar">Your data is safe, read our Privacy Policy</div>

</body>
</html>
```